Get me out of Jail business cards!!!!

I need business cards done for my business. I own a BailBonds and I get people out of jail!

Colors are red white and black

I need it to say on the card these details:

Freedom Hop Bailbonds

427 S Calloway St
Palmetto Springs, FL 33871

863-555-0187

Open 24/7

On the back of the card:

Must check in every Tuesday.

______/______/______ court date
____________________ time
You must know your court date at all times!

Marla Whitcombe - owner
Jolene Whitcombe - agent
Rosalind Pickett - agent

Industry/Entity Type

Bail bonds

Contact Information for Business Card

Colors are red white and black I need it to say on the card these details: Freedom Hop Bailbonds 427 S Calloway St Palmetto Springs, FL 33871 863-555-0187 Open 24/7 On the back of the card: Must check in every Tuesday. ______/______/______ court date ____________________ time You must know your court date at all times! Marla Whitcombe - owner Jolene Whitcombe - agent Rosalind Pickett - agent

Font styles to use
Serif
Sans Serif

Colors
EB3D1F
EC4F4E
F09395
F8D3D4
FCEDEE

Requirements
Must have
• I listed the must haves in the business card details
Nice to have
• Handcuffs or jail bars or a man in a black and white suit

```html
<!DOCTYPE html>
<html lang="en">
<head>
<meta charset="utf-8">
<title>Freedom Hop Bailbonds – Business Cards</title>
<link href="https://fonts.googleapis.com/css2?family=Questrial&family=Montserrat:wght@600&family=Archivo+Narrow&family=Arimo&display=swap" rel="stylesheet">
<style>
  :root {
    --bg: #2b2b2d;
    --card-red: #e60000;
    --card-black: #000000;
    --accent-red: #e8000b;
    --white: #ffffff;
    --divider: #5a5a5a;
  }
  * { margin: 0; padding: 0; box-sizing: border-box; }
  html, body { width: 1200px; height: 912px; overflow: hidden; }
  body { background: var(--bg); position: relative; font-family: "Questrial", sans-serif; }

  .card {
    position: absolute;
    left: 250px;
    width: 700px;
    height: 400px;
    border-radius: 24px;
    overflow: hidden;
  }

  /* Reverse side */
  .card-back { top: 36px; background: var(--card-red); color: var(--white); }
  .checkin-title {
    position: absolute; left: 92px; top: 108px;
    font-family: "Montserrat", sans-serif; font-weight: 600; font-size: 25px;
  }
  .fill-line {
    position: absolute; left: 110px;
    display: flex; align-items: flex-end; gap: 4px;
    font-size: 19px;
  }
  .fill-line .blank { display: inline-block; border-bottom: 1.5px solid var(--white); height: 22px; }
  .court-date { top: 150px; }
  .court-date .blank { width: 62px; }
  .court-time { top: 186px; }
  .court-time .blank { width: 202px; }
  .fill-line .label { margin-left: 6px; }
  .reminder {
    position: absolute; left: 200px; top: 300px;
    font-size: 20px; letter-spacing: 0.2px;
  }

  /* Front side */
  .card-front { top: 476px; background: var(--card-black); color: var(--white); }
  .brand-name {
    position: absolute; left: 34px; top: 188px; width: 360px;
    font-family: "Questrial", sans-serif; font-size: 30px; color: var(--white);
    text-align: center;
  }
  .divider {
    position: absolute; left: 408px; top: 34px;
    width: 1px; height: 260px; background: var(--divider);
  }
  .team { position: absolute; left: 430px; top: 42px; }
  .member-name {
    font-family: "Montserrat", sans-serif; font-weight: 600;
    font-size: 23px; color: var(--accent-red); line-height: 1.05;
  }
  .member-role { font-family: "Arimo", sans-serif; font-size: 15px; margin: 2px 0 10px 4px; }
  .contact {
    position: absolute; left: 434px; top: 232px;
    font-family: "Arimo", sans-serif; font-size: 16px; line-height: 1.25;
  }
  .contact .hours { margin-top: 14px; }
  .contact .phone { display: flex; align-items: center; gap: 6px; }
  .footer-rule {
    position: absolute; left: 0; right: 0; bottom: 46px;
    height: 3px; background: var(--white);
  }
  .footer-band {
    position: absolute; left: 0; right: 0; bottom: 0; height: 40px;
    background: var(--accent-red);
    display: flex; align-items: center; justify-content: flex-end; padding-right: 168px;
    font-family: "Archivo Narrow", sans-serif; font-size: 20px; color: var(--white);
  }
</style>
</head>
<body>

<section class="card card-back" aria-label="Card reverse">
  <p class="checkin-title">Must check in every Tuesday</p>
  <p class="fill-line court-date"><span class="blank"></span>/<span class="blank"></span>/<span class="blank"></span><span class="label">court date</span></p>
  <p class="fill-line court-time"><span class="blank"></span><span class="label">time</span></p>
  <p class="reminder">You must know your court date at all times!</p>
</section>

<section class="card card-front" aria-label="Card front">
  <p class="brand-name">Freedom Hop Bailbonds</p>
  <div class="divider"></div>
  <div class="team">
    <p class="member-name">Marla Whitcombe</p>
    <p class="member-role">owner</p>
    <p class="member-name">Jolene Whitcombe</p>
    <p class="member-role">agent</p>
    <p class="member-name">Rosalind Pickett</p>
    <p class="member-role">agent</p>
  </div>
  <div class="contact">
    <p>427 S Calloway St</p>
    <p>Palmetto Springs, FL 33871</p>
    <p class="hours">Open 24/7</p>
    <p class="phone">
      <svg width="14" height="14" viewBox="0 0 24 24" aria-hidden="true"><path fill="#e8000b" d="M6.6 10.8a15.1 15.1 0 0 0 6.6 6.6l2.2-2.2c.3-.3.7-.4 1-.2 1.1.4 2.3.6 3.6.6.6 0 1 .4 1 1V20c0 .6-.4 1-1 1A17 17 0 0 1 3 4c0-.6.4-1 1-1h3.5c.6 0 1 .4 1 1 0 1.3.2 2.5.6 3.6.1.3 0 .7-.2 1z"/></svg>
      <span>863-555-0187</span>
    </p>
  </div>
  <div class="footer-rule"></div>
  <div class="footer-band">Freedom Hop Bailbonds</div>
</section>

</body>
</html>
```